Caldrey Orthodontics business card

Using our existing logo (created with PixelGuild), please create a tasteful, contemporary business card. We are father and daughter orthodontists specializing in braces, clearvora, etc to design healthy, beautiful smiles for children, adolescents, and adults. We would like the design to be family-friendly but not childish.
The final design should include all of the information without looking cluttered (I hope! If necessary to achieve an optimal design, please consider making the card double-sided)
Purple, black, silver on a white card
Please include the following information:
Caldrey Orthodontics (logo)
Marisol T. Caldrey, DMD
Gordon L. Caldrey, DMD

312 Hollowmere Road
Ashbrook Falls, MA 01990
555.214.3096

748C Brackenford Lane
Lindell Park, MA 01992
555.407.1582

email frontdesk@caldreyortho-example.com
website www.caldreyortho-example.com

```html
<!DOCTYPE html>
<html lang="en">
<head>
<meta charset="utf-8">
<title>Caldrey Orthodontics business card</title>
<link href="https://fonts.googleapis.com/css2?family=Arimo&family=Tinos:wght@700&display=swap" rel="stylesheet">
<style>
  :root {
    --purple: #5c2a8a;
    --purple-deep: #4f2379;
    --silver: #7d7d7d;
    --card-white: #f5f5f6;
    --ink-light: #ffffff;
    --backdrop: #dedede;
  }
  html, body {
    margin: 0;
    width: 1200px;
    height: 1040px;
    overflow: hidden;
    background: var(--backdrop);
  }
  .canvas { position: relative; width: 1200px; height: 1040px; }
  .card {
    position: absolute;
    left: 200px;
    width: 800px;
    height: 458px;
    border-radius: 22px;
    overflow: hidden;
  }
  .card--front { top: 44px; background: var(--card-white); }
  .card--back { top: 540px; background: var(--purple); }
  .card__wave { position: absolute; inset: 0; }
  .brand {
    position: absolute;
    left: 62px;
    top: 82px;
    display: flex;
    align-items: center;
    gap: 12px;
  }
  .brand__dot { width: 18px; height: 18px; border-radius: 50%; background: var(--purple); }
  .brand__name {
    font-family: "Tinos", serif;
    font-weight: 700;
    font-size: 36px;
    color: var(--purple);
    margin: 0;
  }
  .contact {
    position: absolute;
    right: 28px;
    top: 140px;
    text-align: right;
    font-family: "Arimo", sans-serif;
    font-size: 19px;
    line-height: 25px;
    color: var(--ink-light);
  }
  .contact__block { margin: 0 0 14px; font-style: normal; }
  .contact__row { display: flex; justify-content: flex-end; align-items: center; gap: 8px; }
  .contact__row svg { width: 16px; height: 16px; flex: none; }
  .doctors {
    position: absolute;
    right: 26px;
    top: 378px;
    text-align: right;
    font-family: "Tinos", serif;
    font-weight: 700;
    font-size: 23px;
    line-height: 28px;
    color: var(--ink-light);
    text-transform: uppercase;
    margin: 0;
  }
  .back__mark {
    position: absolute;
    left: 0; right: 0; top: 180px;
    text-align: center;
    font-family: "Tinos", serif;
    font-weight: 700;
    font-size: 44px;
    color: var(--purple-deep);
    margin: 0;
  }
  .back__web {
    position: absolute;
    left: 0; right: 0; top: 396px;
    text-align: center;
    font-family: "Arimo", sans-serif;
    font-size: 20px;
    color: var(--ink-light);
    margin: 0;
  }
</style>
</head>
<body>
<main class="canvas">
  <section class="card card--front" aria-label="Front of card">
    <svg class="card__wave" viewBox="0 0 800 458" aria-hidden="true">
      <path fill="var(--silver)" d="M0,288 C130,350 260,372 360,322 C440,280 520,170 600,110 C670,62 740,58 802,72 L802,82 C740,70 670,85 600,130 C520,190 430,320 340,360 C250,400 130,385 0,320 Z"/>
      <path fill="var(--purple)" stroke="#ffffff" stroke-width="4" d="M-2,320 C130,385 250,400 340,360 C430,320 520,190 600,130 C670,85 740,70 802,82 L802,460 L-2,460 Z"/>
    </svg>
    <div class="brand">
      <span class="brand__dot"></span>
      <h1 class="brand__name">Caldrey Orthodontics</h1>
    </div>
    <div class="contact">
      <address class="contact__block">
        312 Hollowmere Road<br>
        Ashbrook Falls, MA 01990
        <span class="contact__row">555.214.3096
          <svg viewBox="0 0 16 16"><path fill="#fff" d="M3.5 1.5l2.5 3-1.5 1.8c.8 1.8 2.2 3.2 4 4l1.8-1.5 3 2.5-1.6 2.2C7 13.5 2.5 9 1.3 3.1z"/></svg>
        </span>
      </address>
      <address class="contact__block">
        748C Brackenford Lane<br>
        Lindell Park, MA 01992
        <span class="contact__row">555.407.1582
          <svg viewBox="0 0 16 16"><path fill="#fff" d="M3.5 1.5l2.5 3-1.5 1.8c.8 1.8 2.2 3.2 4 4l1.8-1.5 3 2.5-1.6 2.2C7 13.5 2.5 9 1.3 3.1z"/></svg>
        </span>
      </address>
      <div class="contact__row">frontdesk@caldreyortho-example.com
        <svg viewBox="0 0 16 16"><rect x="1" y="3.5" width="14" height="9" fill="#fff"/><path d="M1.5 4l6.5 5 6.5-5" fill="none" stroke="var(--purple)" stroke-width="1.2"/></svg>
      </div>
      <div class="contact__row">www.caldreyortho-example.com
        <svg viewBox="0 0 16 16"><circle cx="8" cy="8" r="7" fill="#fff"/><path d="M4 5c2 0 3 1 2.5 3S8 10 7 13M10 3c0 2 2 2 3.5 3" fill="none" stroke="var(--purple)" stroke-width="1.5"/></svg>
      </div>
    </div>
    <p class="doctors">Marisol T. Caldrey, DMD<br>Gordon L. Caldrey, DMD</p>
  </section>

  <section class="card card--back" aria-label="Back of card">
    <p class="back__mark">Caldrey Orthodontics</p>
    <p class="back__web">www.caldreyortho-example.com</p>
  </section>
</main>
</body>
</html>
```